Web design for boutique law firm

Web design for law firm; practice areas include:
-international intellectual property counseling
-general corporate (contract negotiation, licensing, distribution agreements
-see my *very* outdated website at www.pvtlegalhouse.com: here is some of the home page content:

"PVT Law Group enjoys providing proactive, business-minded, efficient legal solutions for individuals and companies that benefit from major law firm experience at reasonable rates.

Some areas of emphasis include:

Counseling individuals and companies with respect to clearing, selecting, securing, managing, commercializing, and protecting intellectual property assets around the world. This includes traditional global brand management, marketing, advertising, and enforcement work as well as litigation.
PVT Law Group also provides general counseling services for individuals and businesses, from start-up advice to sophisticated business transactions strategy, agreement negotiating, dispute resolution, and litigation.
Before founding PVT Law Group in 2008, Curtis L. Abernathy led the Trademark, Copyright, & Brand Management Group for Falkner & Ingleby's Seattle office. Curtis was also a senior associate at Silicon Valley based Hartwell, Bexley, Oduya, & Penrose."

Target Market(s)

Clients/potential clients needing tier one, international intellectual property advice with "mega" law firm experience for much less than what we were/would be charging at the "mega firms".

Industry/Entity Type

Legal

Number of Pages Required

4 page

Font styles to use
Serif
Sans Serif

Colors

Designer to choose colors to be used in the design.

Requirements
Must have
• +Improvement over everything on current site at www.pvtlegalhouse.com.
• +Pictures/bios for me and my team (four of us right now).
• +Easy to update and add/remove content.
• +Must be superior in design (look, feel, ease of use, classy and elegant, but hip, reflects international practice).
• +i have logos and color schemes (see current website) but will consider improvements.
Nice to have
• Let me know your thoughts.
Should not have
• No cheese; no overt sales pitches or marketing (since law firm).

```html
<!DOCTYPE html>
<html lang="en">
<head>
<meta charset="utf-8">
<title>Experience | PVT Law Group</title>
<link href="https://fonts.googleapis.com/css2?family=Open+Sans:wght@400;600;700;800&display=swap" rel="stylesheet">
<style>
:root{
  --brand:#b32a1f;
  --ink:#444;
  --muted:#6a6a6a;
  --rule:#d9d9d9;
  --paper:#ffffff;
  --footer:#3b3b3b;
  --footer-ink:#bdbdbd;
}
*{margin:0;padding:0;box-sizing:border-box}
html,body{width:1200px;height:2180px;overflow:hidden;background:var(--paper)}
body{font-family:"Open Sans",Arial,sans-serif;color:var(--ink);position:relative;font-size:14px}
.site-header{height:80px;display:flex;align-items:center;justify-content:space-between;padding:0 48px;border-bottom:1px solid var(--rule)}
.brand{font-weight:600;font-size:18px;color:var(--ink)}
.main-nav{display:flex;gap:6px}
.main-nav a{font-size:12px;font-weight:700;letter-spacing:1px;color:var(--muted);text-decoration:none;padding:10px 20px}
.main-nav a.active{background:var(--brand);color:#fff}
.content{padding:0 48px}
.page-title{font-size:34px;font-weight:800;color:var(--brand);letter-spacing:1px;margin-top:58px;padding-bottom:12px;border-bottom:2px solid var(--brand)}
.section{border-bottom:1px dashed var(--rule);padding:26px 0 34px}
.section h2{font-size:17px;font-weight:700;color:var(--brand);margin-bottom:16px}
.bullets{list-style:none}
.bullets li{line-height:23px;margin-bottom:12px;padding-left:16px;position:relative}
.bullets li::before{content:"•";position:absolute;left:0;color:var(--brand)}
.bullets.tight li{margin-bottom:6px}
.bullets b{font-weight:700;color:#333}
.bullets .sub{padding-left:18px}
.bullets .sub li{margin-bottom:2px}
.intro{line-height:23px;margin-bottom:18px}
.clients{list-style:none;columns:2;column-gap:40px;width:680px}
.clients li{line-height:22.5px;padding-left:16px;position:relative}
.clients li::before{content:"•";position:absolute;left:0;color:var(--brand)}
.site-footer{position:absolute;left:0;right:0;bottom:0;height:60px;background:var(--footer);color:var(--footer-ink);display:flex;align-items:center;justify-content:center;gap:16px;font-size:12px}
.site-footer span.sep{color:#777}
</style>
</head>
<body>
<header class="site-header">
  <div class="brand">PVT Law Group</div>
  <nav class="main-nav">
    <a href="#">HOME</a><a href="#">ABOUT</a><a href="#">TEAM</a><a href="#" class="active">EXPERIENCE</a><a href="#">CONTACT</a>
  </nav>
</header>

<main class="content">
  <h1 class="page-title">EXPERIENCE</h1>

  <section class="section">
    <h2>Representative Experience:</h2>
    <ul class="bullets">
      <li><b>Brand Management</b> - Managed global brand portfolios for consumer brands, including trademark clearance, prosecution, enforcement, maintenance, sponsorship, licensing, distribution, domain name matters, and litigation/contentious matters.</li>
      <li><b>Brand Enforcement</b> - Established strategy for and resolved complex multi-jurisdictional intellectual property disputes.</li>
      <li><b>Counterfeiting</b> - Coordinated enforcement strategy with consumer electronic client against a U.S. Korean counterfeiter in coordination with U.S. Customs &amp; Border Protection.</li>
      <li><b>Litigation</b> - Managed litigation, client's relationship and expectations (substantive and fiscal), and assisted with case strategy, in trademark infringement suit that settled for near-defendants' initial monetary offer. Assisted with and attended key depositions. Managed and prepared secondary meaning expert in product configuration trade dress litigation.</li>
      <li><b>Rebranding</b> - Worked directly with CEO to re-brand a publicly traded tech company.</li>
      <li><b>Due Diligence</b> - Conducted intellectual property due diligence for underwriting institutions (financings and IPOs) and companies (financings and M&amp;A transactions).</li>
      <li><b>IP Counsel and Management</b> - Managed worldwide domain name, trademark, and patent portfolio for large OEM/ODM, including its 35 subsidiaries; transferred assets to related company for tax and intellectual property portfolio management purposes.</li>
      <li><b>Domain Names</b> - Provide proactive global procurement strategies for domain names; negotiated domain name transfers under the UDRP.</li>
    </ul>
  </section>

  <section class="section">
    <h2>Representative Work:</h2>
    <p class="intro">Over the years, Curtis has worked on brand identity/trademark and domain name related matters for:</p>
    <ul class="clients">
      <li>Orchardline</li><li>WideReach Networks</li><li>Harborside Pizza</li><li>Campus Chalkworks</li><li>Pedalwise LLC</li><li>Marlowe Institute of Technology</li><li>N-S Construction</li><li>Rowan &amp; Pike, Incorporated</li><li>Travelquill</li><li>Halvorsen Trust</li><li>Brennan Holt Inc. dba Estatecrest.com</li><li>Tolliver's Burger Works</li><li>Vantor Holdings</li><li>Ashgrove Capital</li>
      <li>Miss Tansy LLC</li><li>Kellerman Partners</li><li>Tidewell Fitness</li><li>Clearview Surgical Imaging</li><li>Verdance Bio Alliance</li><li>StageBright Inc.</li><li>Frondline</li><li>Cedar Hollow Vineyards</li><li>Quarrystore</li><li>Brightwater Banks Inc.</li><li>Educators Across Borders</li><li>Norland Bank</li>
    </ul>
  </section>

  <section class="section">
    <h2>Honors/Law Firm Activities:</h2>
    <ul class="bullets tight">
      <li>Named a Rising Star, Northwest Counsel Review, 2006, 2007, &amp; 2008</li>
      <li>Member of Falkner Seattle Recruiting Committee</li>
    </ul>
  </section>

  <section class="section">
    <h2>Memberships/Law Firm Activities:</h2>
    <ul class="bullets tight">
      <li>Member, Global Brand Owners Association's Online Existing Content Evaluation Subcommittee for Information Resources Committee - 2010-2011 Term</li>
      <li>Member, Subcommittee for Information Resources Committee - 2008-2009 Term</li>
      <li>Member, Regional Bar Association, 2003 to present</li>
      <li>Counseled pro bono clients; Survivors Celebration Foundation, with branding strategies and entity formation, 2008</li>
      <li>Member, Business Development Sub-Committee, Fieldwork, 2002-2003</li>
    </ul>
  </section>

  <section class="section">
    <h2>Honors/Law Firm Activities:</h2>
    <ul class="bullets tight">
      <li>"Protecting Your Intellectual Property", Summit Trade Alliance's Legally Speaking Series: "What Every Early Stage Entrepreneur Should Know About Building A Successful Company", October 2005 and March 2006</li>
      <li>"Intellectual Property Legal Issues for New Ventures", Harborview University School of Business, November 2005</li>
    </ul>
  </section>

  <section class="section" style="border-bottom:0">
    <h2>Education:</h2>
    <ul class="bullets tight">
      <li>Cedarbrook University College of Law, J.D., cum laude, 2001
        <ul class="bullets sub">
          <li>Editor, Cedarbrook Law and Technology Journal</li>
          <li>Research Assistant for the late Professor Richard L. Ashcombe</li>
          <li>Extern for the United States Attorney's Office / Northern District of New York</li>
          <li>Clerk, Honorable Judge Hedges - New York Family Law Court</li>
          <li>Clerk, Honorable Judge Centeno - New York State Supreme Court</li>
        </ul>
      </li>
      <li>Ridgeline State University, B.A., cum laude, 1998</li>
    </ul>
  </section>
</main>

<footer class="site-footer">
  <span>© 2008-2017 PVT LAW GROUP PLLC | All rights reserved</span>
  <span class="sep">|</span>
  <span>www.pvtlegalhouse.com</span>
</footer>
</body>
</html>
```